Our Kitchen Pantry is an online food market place that connects foodies who make or grow great food with

We would like a 1/2 A4 page size flyer in landscape to promote our new business. We would like to encourage new home foodies to sign up for a membership on our website www.ourkitchenpantrynz.co.nz and we would like customers who are looking for great food in their local community to search our website for their closest home foodie and support a neighbour who is growing or producing creative food locally

Target Market(s)

Creative food lovers

Industry/Entity Type

Landscape

Colors
acd037
f78f20
33b8a4

Requirements
Must have
• Food images and look groovy
• Must be easy to read and stand out on a notice board
• Website address www.ourkitchenpantrynz.co.nz
Nice to have
• We wish to use this flyer in multiple locations and wish to put in different contact details prior to printing

```html
<!DOCTYPE html>
<html lang="en">
<head>
<meta charset="utf-8">
<title>Our Kitchen Pantry – Flyer</title>
<link href="https://fonts.googleapis.com/css2?family=Varela+Round&display=swap" rel="stylesheet">
<style>
  :root {
    --green: #77bf43;
    --orange: #f7901f;
    --teal: #33b8a4;
    --cream: #f2e18e;
    --tan: #c9b08c;
    --brown: #4a2411;
  }
  * { margin: 0; padding: 0; box-sizing: border-box; }
  html, body { width: 1200px; height: 846px; overflow: hidden; }
  body { font-family: "Varela Round", "Trebuchet MS", sans-serif; }

  .flyer {
    position: relative;
    width: 1200px;
    height: 846px;
    background: linear-gradient(to bottom,
      var(--green) 0, var(--green) 424px,
      var(--teal) 424px, var(--teal) 450px,
      var(--orange) 450px, var(--orange) 100%);
    color: var(--cream);
    overflow: hidden;
  }

  .headline {
    position: absolute;
    top: 26px; left: 0; width: 100%;
    text-align: center;
    font-size: 39px;
    line-height: 50px;
  }

  .pitch {
    position: absolute;
    text-align: center;
    font-size: 28px;
    line-height: 33.5px;
  }
  .pitch--seller { top: 317px; left: 30px; width: 300px; }
  .pitch--buyer  { top: 284px; left: 860px; width: 300px; }

  .brand {
    position: absolute;
    left: 345px; top: 170px;
    width: 480px; height: 480px;
  }
  .brand__disc { position: absolute; inset: 0; }
  .brand__name {
    position: absolute;
    inset: 0;
    display: flex;
    align-items: center;
    justify-content: center;
    text-align: center;
    font-size: 72px;
    line-height: 80px;
    color: var(--brown);
  }

  .web-address {
    position: absolute;
    top: 692px; left: 0; width: 100%;
    text-align: center;
    font-size: 41px;
  }
</style>
</head>
<body>
  <main class="flyer">
    <h1 class="headline">Be part of our exciting new online food marketplace connecting<br>foodies in your local community!</h1>

    <p class="pitch pitch--seller">As a foodie you can sell your beautiful home produced or home grown produce on our marketplace website</p>

    <div class="brand">
      <svg class="brand__disc" viewBox="0 0 480 480" aria-hidden="true">
        <circle cx="240" cy="240" r="238" fill="var(--tan)"/>
      </svg>
      <p class="brand__name">Our<br>Kitchen<br>Pantry</p>
    </div>

    <p class="pitch pitch--buyer">As a food lover you can purchase lovingly grown or prepared food and support your local foodie community while keeping your food miles low</p>

    <p class="web-address">www.ourkitchenpantrynz.co.nz</p>
  </main>
</body>
</html>
```